Business Card - Rebranding for Consulting Firm

We are renaming and rebranding our consulting firm and need to raise the level of quality of our cards as part of that effort. We consult to leading high tech, life science and other innovation sector companies.

Need a two-sided business card design.

Side 1: (a) Company logo (b) tag line: Optimize Your Investment in Talent (c) Name (d) Title (e) Phone 1: Office (f) Phone 2: Mobile (g) email: person@QuillharborAdvisory.com

Side 2: Two lines of text: (a) Growth is Imperative. Change is Constant. Talent Executes Strategy. (b) We help you excel at all three.

Target Market(s)

Business and human resources executives and senior managers

Industry/Entity Type

Management Consulting

Contact Information for Business Card

Font styles to use
Sans Serif

Requirements
Must have
• clean, not too busy, but with a bit of creativity. Stick to the colors used in the attached logo
• appeal to high tech, life science companies
Nice to have
• prefer white background

```html
<!DOCTYPE html>
<html lang="en">
<head>
<meta charset="utf-8">
<title>Quillharbor Advisory – Business Card</title>
<link rel="stylesheet" href="https://fonts.googleapis.com/css2?family=Open+Sans:ital,wght@0,400;0,600;0,700;1,400&display=swap">
<style>
  :root {
    --brand-blue: #1766a8;
    --band-grey: #6f8291;
    --ink: #1c1c1c;
    --muted-ink: #5d6f7c;
    --paper: #ffffff;
    --backdrop: #3a3a3c;
  }
  * { box-sizing: border-box; margin: 0; padding: 0; }
  html, body { width: 1200px; height: 900px; overflow: hidden; }
  body {
    background: var(--backdrop);
    font-family: "Open Sans", Arial, sans-serif;
    position: relative;
  }
  .card {
    position: absolute;
    width: 720px;
    height: 410px;
    background: var(--paper);
    box-shadow: 0 10px 28px rgba(0,0,0,0.45);
    overflow: hidden;
  }
  .card--back { left: 400px; top: 30px; }
  .card--front { left: 80px; top: 465px; }

  .wordmark {
    display: flex;
    align-items: center;
    gap: 12px;
    color: var(--brand-blue);
    font-weight: 600;
    font-size: 36px;
    letter-spacing: -0.5px;
    line-height: 1;
  }
  .wordmark__square {
    width: 28px; height: 28px;
    background: var(--brand-blue);
    flex: none;
  }

  /* reverse side */
  .card--back .wordmark { justify-content: center; margin-top: 120px; }
  .statement {
    margin-top: 48px;
    text-align: center;
    font-style: italic;
    color: var(--muted-ink);
    font-size: 19px;
    line-height: 1.5;
  }
  .statement__emphasis { text-transform: uppercase; }

  /* front side */
  .card--front .wordmark { position: absolute; left: 80px; top: 50px; }
  .person {
    position: absolute;
    right: 60px; top: 100px;
    text-align: right;
  }
  .person__name {
    color: var(--brand-blue);
    font-weight: 700;
    font-size: 27px;
    line-height: 1.1;
  }
  .person__title {
    color: var(--ink);
    font-size: 19px;
    margin-top: 4px;
  }
  .divider {
    position: absolute;
    left: 150px; right: 50px; top: 172px;
    height: 2px;
    background: var(--brand-blue);
  }
  .contact {
    position: absolute;
    left: 40px; top: 192px;
    list-style: none;
    color: var(--ink);
    font-size: 17px;
    line-height: 1.6;
  }
  .contact__item { display: flex; align-items: center; gap: 12px; }
  .contact__icon { width: 16px; height: 16px; fill: var(--brand-blue); flex: none; }

  .footer-band {
    position: absolute;
    left: 0; bottom: 0;
    width: 720px; height: 80px;
  }
  .tagline {
    position: absolute;
    right: 30px; bottom: 18px;
    color: var(--paper);
    font-size: 22px;
    white-space: nowrap;
  }
</style>
</head>
<body>

  <section class="card card--back" aria-label="Business card, reverse side">
    <div class="wordmark">
      <span class="wordmark__square"></span>
      <span class="wordmark__name">Quillharbor Advisory</span>
    </div>
    <p class="statement">
      Growth is Imperative. Change is Constant. Talent Executes Strategy.<br>
      <span class="statement__emphasis">We help you excel at all three.</span>
    </p>
  </section>

  <section class="card card--front" aria-label="Business card, front side">
    <div class="wordmark">
      <span class="wordmark__square"></span>
      <span class="wordmark__name">Quillharbor Advisory</span>
    </div>

    <div class="person">
      <p class="person__name">Maren Holt</p>
      <p class="person__title">Manager</p>
    </div>

    <div class="divider"></div>

    <ul class="contact">
      <li class="contact__item">
        <svg class="contact__icon" viewBox="0 0 16 16" aria-hidden="true">
          <path d="M3.5 1.5 6 4 4.8 5.8c.8 1.9 2.3 3.4 4.2 4.2L10.8 8.8 13.5 11.3 12 14C6.5 13.5 2.5 9.5 2 4z"/>
        </svg>
        <span>512 555 0148</span>
      </li>
      <li class="contact__item">
        <svg class="contact__icon" viewBox="0 0 16 16" aria-hidden="true">
          <path d="M4.5 1h7a1 1 0 0 1 1 1v12a1 1 0 0 1-1 1h-7a1 1 0 0 1-1-1V2a1 1 0 0 1 1-1zm.5 2v8h6V3zm3 9.2a.9.9 0 1 0 0 1.8.9.9 0 0 0 0-1.8z"/>
        </svg>
        <span>512 555 0149</span>
      </li>
      <li class="contact__item">
        <svg class="contact__icon" viewBox="0 0 16 16" aria-hidden="true">
          <path d="M1 3.5h14v9H1zm1.3 1 5.7 4.3 5.7-4.3zM2 5.6V11.5h12V5.6L8 10.1z"/>
        </svg>
        <span>person@QuillharborAdvisory.com</span>
      </li>
    </ul>

    <svg class="footer-band" viewBox="0 0 720 80" aria-hidden="true">
      <rect x="0" y="30" width="720" height="50" fill="var(--band-grey)"/>
      <path d="M196 80 C228 80 228 14 278 14 H720 V80 Z" fill="var(--paper)"/>
      <path d="M208 80 C238 80 238 20 286 20 H720 V80 Z" fill="var(--brand-blue)"/>
    </svg>
    <p class="tagline">Optimize Your Investment in Talent</p>
  </section>

</body>
</html>
```